creating a design for an eyelash box/logo

I want to create a design for an eyelash box that will have our company name on it as well which is "Mirela Brows" we create cruelty free mink false lashes. Mirela is a Russian name and I want to give it a luxury and feminine floral feel. I want to add a caption on the back of the box that says "no minks were harmed in the making of these lashes" I have included some inspiration pictures in the upload files. I am thinking i want to base of the box to be black and then Mirela Brows in the middle with maybe gold lettering but im up for suggestions and then the perimeter of the box russian floral patterns,Like i said i added photos of the color scheme that i like so i want options with these different colors. I want Mirela Brows to have a cursive style writing. I also added a photo of the size of the box but ignore the actual design on it. I hope this helps! thanks
Updates

Target Market(s)

young women who want to look gorgeous (can be men too:) )

Industry/Entity Type

It Company

Font styles to use
Script

Requirements
Must have
• floral design
Nice to have
• i added photos of what i want to perimeter to look like
Should not have
• not sure

```html
<!DOCTYPE html>
<html lang="en">
<head>
<meta charset="utf-8">
<title>Mirela Brows – Lash Box Lid</title>
<link rel="stylesheet" href="https://fonts.googleapis.com/css2?family=Pinyon+Script&display=swap">
<style>
  :root {
    --page: #efe9e1;
    --board: #3b3336;
    --heart: #352e31;
    --rose-magenta: #c81f9c;
    --rose-red: #c92a2f;
    --rose-pink: #d776b6;
    --leaf-green: #35b862;
    --gold-light: #f3e6b4;
    --gold: #d9b548;
    --gold-deep: #b98a22;
  }
  * { margin: 0; padding: 0; box-sizing: border-box; }
  html, body {
    width: 1200px;
    height: 768px;
    overflow: hidden;
    background: var(--page);
  }
  .lid {
    position: relative;
    width: 1200px;
    height: 768px;
    background: var(--board);
    overflow: hidden;
  }
  .floral-border {
    position: absolute;
    inset: 0;
    background:
      linear-gradient(180deg, rgba(59, 51, 54, 0) 0%, rgba(59, 51, 54, 0.25) 100%),
      linear-gradient(125deg,
        var(--rose-magenta) 0%,
        var(--rose-red) 22%,
        var(--rose-pink) 40%,
        var(--leaf-green) 55%,
        var(--rose-magenta) 72%,
        var(--rose-red) 100%);
  }
  .gold-edge {
    position: absolute;
    inset: 8px;
    border: 2px solid var(--gold);
    pointer-events: none;
  }
  .heart-field {
    position: absolute;
    inset: 0;
    width: 1200px;
    height: 768px;
  }
  .heart-field path { fill: var(--heart); }
  .brand-mark {
    position: absolute;
    left: 50%;
    top: 180px;
    transform: translateX(-50%);
    display: flex;
    align-items: center;
    gap: 16px;
  }
  .brand-mark__circle {
    width: 48px;
    height: 48px;
    border: 3px solid var(--gold);
    border-radius: 50%;
    flex: none;
  }
  .brand-mark__name {
    font-family: "Pinyon Script", cursive;
    font-size: 44px;
    line-height: 1;
    color: var(--gold);
    white-space: nowrap;
  }
  .wordmark {
    position: absolute;
    left: 0;
    right: 0;
    top: 350px;
    text-align: center;
    font-family: "Pinyon Script", cursive;
    font-weight: 400;
    font-size: 118px;
    line-height: 1.1;
    white-space: nowrap;
    background: linear-gradient(180deg, var(--gold-light) 0%, var(--gold) 55%, var(--gold-deep) 100%);
    -webkit-background-clip: text;
    background-clip: text;
    color: transparent;
  }
</style>
</head>
<body>
  <main class="lid">
    <div class="floral-border" role="img" aria-label="Border pattern of magenta, red and pink roses with green leaves on a dark ground"></div>
    <svg class="heart-field" viewBox="0 0 1200 768" aria-hidden="true">
      <path d="M600 200 C540 60 300 20 150 110 C20 200 40 420 190 560 C320 680 500 720 600 752 C700 720 880 680 1010 560 C1160 420 1180 200 1050 110 C900 20 660 60 600 200 Z"/>
    </svg>
    <div class="gold-edge" aria-hidden="true"></div>
    <div class="brand-mark">
      <span class="brand-mark__circle"></span>
      <span class="brand-mark__name">Mirela Brows</span>
    </div>
    <h1 class="wordmark">Mirela Brows</h1>
  </main>
</body>
</html>
```